Hearth And Loom Biz Card Design

That example is too complicated. Hearth And Loom is my home design business.

I design Interiors, Exteriors and Home Staging.

My tag line is: BRINGING BRIGHT IDEAS TO INTERIORS, EXTERIORS AND HOME STAGING.

I would like a clean, simple, modern (sort of Helvetica-ish) design that includes an image of a light bulb. The bulb and the text should blend seamlessly.

I prefer a white background; black text; and blue highlights (lightbulb); not a greenish blue, not a navy blue. A color that mixes the best of both. Green/Blue. Not turquoise.

The color scheme should be elegant. And modern. Professional. Not quite 'too hip for the room'.

Sorta ignore the logo design example that is attached.

Let me know any questions! Look forward, thank you Carla

Business

Carla M Vandrell
Senior Design Specialist
Tel: 310-574-2936
Web: carla@hearthandloomhome.com

• Font and color

```html
<!DOCTYPE html>
<html lang="en">
<head>
<meta charset="utf-8">
<title>Hearth And Loom – Business Card Concepts</title>
<link href="https://fonts.googleapis.com/css2?family=Anton&family=Questrial&family=Open+Sans:ital,wght@0,400;1,400&family=Roboto+Condensed:wght@400&display=swap" rel="stylesheet">
<style>
  :root {
    --paper: #ffffff;
    --ink: #1a1a1a;
    --ink-soft: #444444;
    --rule-grey: #6b6b6b;
    --teal-blue: #2b8fc6;
    --deep-blue: #2f4fa3;
    --rule-blue: #3a78c2;
    --rule-fade: #dfe6f2;
  }
  * { margin: 0; padding: 0; box-sizing: border-box; }
  html, body {
    width: 1200px; height: 801px; overflow: hidden;
    background: var(--paper);
  }
  .board { position: relative; width: 1200px; height: 801px; }

  .option-number {
    position: absolute;
    font-family: "Anton", "Impact", sans-serif;
    font-size: 64px; line-height: 1; color: #000;
  }

  .card { position: absolute; width: 500px; height: 240px; }
  .card-rules { position: absolute; inset: 0; width: 500px; height: 240px; }

  .brand {
    position: absolute; left: 24px; top: 30px;
    display: flex; align-items: center; gap: 10px;
  }
  .brand-dot {
    width: 30px; height: 30px; border-radius: 50%;
    background: var(--deep-blue);
  }
  .brand--teal .brand-dot { background: var(--teal-blue); }
  .brand-name {
    font-family: "Questrial", "Helvetica Neue", Arial, sans-serif;
    font-size: 31px; color: var(--ink); letter-spacing: 0.2px;
    line-height: 1;
  }
  .service-line {
    position: absolute; left: 24px; top: 68px;
    font-family: "Roboto Condensed", "Arial Narrow", sans-serif;
    font-size: 11px; color: var(--ink); letter-spacing: 0.1px;
    white-space: nowrap;
  }

  .contact {
    position: absolute; left: 330px; width: 175px;
    text-align: center;
    font-family: "Open Sans", "Helvetica Neue", Arial, sans-serif;
    color: var(--ink-soft);
  }
  .contact-name { font-size: 15px; color: var(--ink); line-height: 18px; }
  .contact-title { font-size: 8px; font-style: italic; color: var(--ink); line-height: 12px; }
  .contact-phone { font-size: 12.5px; line-height: 16px; }
  .contact-email { font-size: 9px; line-height: 12px; }
</style>
</head>
<body>
<main class="board">

  <div class="option-number" style="left:228px; top:6px;">1</div>
  <div class="option-number" style="left:843px; top:8px;">2</div>
  <div class="option-number" style="left:273px; top:716px;">3</div>
  <div class="option-number" style="left:808px; top:710px;">4</div>

  <!-- Option 1 -->
  <section class="card" style="left:99px; top:125px;">
    <svg class="card-rules" viewBox="0 0 500 240" aria-hidden="true">
      <defs>
        <linearGradient id="fadeInRight" x1="0" x2="1">
          <stop offset="0" stop-color="#ffffff"/><stop offset="0.55" stop-color="var(--rule-fade)"/><stop offset="1" stop-color="var(--rule-blue)"/>
        </linearGradient>
        <linearGradient id="fadeOutRight" x1="0" x2="1">
          <stop offset="0" stop-color="var(--rule-blue)"/><stop offset="0.6" stop-color="var(--rule-fade)"/><stop offset="1" stop-color="#ffffff"/>
        </linearGradient>
      </defs>
      <line x1="0" y1="4" x2="491" y2="4" stroke="var(--rule-grey)" stroke-width="1"/>
      <rect x="200" y="5.5" width="291" height="2" fill="url(#fadeInRight)"/>
      <rect x="10" y="101" width="481" height="2" fill="url(#fadeOutRight)"/>
      <line x1="10" y1="105" x2="491" y2="105" stroke="var(--rule-grey)" stroke-width="1"/>
    </svg>
    <div class="brand brand--teal"><span class="brand-dot"></span><span class="brand-name">Hearth And Loom</span></div>
    <div class="service-line">THOUGHTFUL DESIGN FOR EVERY ROOM, EVERY PORCH AND EVERY HOME SALE</div>
    <div class="contact" style="top:164px;">
      <div class="contact-name">Carla M Vandrell</div>
      <div class="contact-title">Senior Design Specialist</div>
      <div class="contact-phone">310.574.2936</div>
      <div class="contact-email">carla@hearthandloomhome.com</div>
    </div>
  </section>

  <!-- Option 2 -->
  <section class="card" style="left:625px; top:125px;">
    <svg class="card-rules" viewBox="0 0 500 240" aria-hidden="true">
      <defs>
        <linearGradient id="fadeInRight2" x1="0" x2="1">
          <stop offset="0" stop-color="#ffffff"/><stop offset="0.5" stop-color="var(--rule-fade)"/><stop offset="1" stop-color="var(--rule-blue)"/>
        </linearGradient>
        <linearGradient id="fadeOutRight2" x1="0" x2="1">
          <stop offset="0" stop-color="var(--rule-blue)"/><stop offset="0.6" stop-color="var(--rule-fade)"/><stop offset="1" stop-color="#ffffff"/>
        </linearGradient>
      </defs>
      <line x1="0" y1="4" x2="491" y2="4" stroke="var(--rule-grey)" stroke-width="1"/>
      <rect x="0" y="5.5" width="491" height="2" fill="url(#fadeInRight2)"/>
      <rect x="10" y="100" width="481" height="2" fill="url(#fadeOutRight2)"/>
      <line x1="10" y1="104" x2="491" y2="104" stroke="var(--ink)" stroke-width="1"/>
    </svg>
    <div class="brand"><span class="brand-dot"></span><span class="brand-name">Hearth And Loom</span></div>
    <div class="service-line">THOUGHTFUL DESIGN FOR EVERY ROOM, EVERY PORCH AND EVERY HOME SALE</div>
    <div class="contact" style="top:164px;">
      <div class="contact-name">Carla M Vandrell</div>
      <div class="contact-title">Senior Design Specialist</div>
      <div class="contact-phone">310.574.2936</div>
      <div class="contact-email">carla@hearthandloomhome.com</div>
    </div>
  </section>

  <!-- Option 3 -->
  <section class="card" style="left:99px; top:418px;">
    <svg class="card-rules" viewBox="0 0 500 240" aria-hidden="true">
      <defs>
        <linearGradient id="fadeOutRight3" x1="0" x2="1">
          <stop offset="0" stop-color="var(--deep-blue)"/><stop offset="0.65" stop-color="var(--rule-fade)"/><stop offset="1" stop-color="#ffffff"/>
        </linearGradient>
      </defs>
      <path d="M12 202 V210 Q12 215 18 215 H481" fill="none" stroke="url(#fadeOutRight3)" stroke-width="2"/>
      <line x1="10" y1="219" x2="481" y2="219" stroke="var(--rule-grey)" stroke-width="1"/>
    </svg>
    <div class="brand"><span class="brand-dot"></span><span class="brand-name">Hearth And Loom</span></div>
    <div class="service-line">THOUGHTFUL DESIGN FOR EVERY ROOM, EVERY PORCH AND EVERY HOME SALE</div>
    <div class="contact" style="top:150px;">
      <div class="contact-name">Carla M Vandrell</div>
      <div class="contact-title">Senior Design Specialist</div>
      <div class="contact-phone">310.574.2936</div>
      <div class="contact-email">carla@hearthandloomhome.com</div>
    </div>
  </section>

  <!-- Option 4 -->
  <section class="card" style="left:625px; top:418px;">
    <svg class="card-rules" viewBox="0 0 500 240" aria-hidden="true">
      <defs>
        <linearGradient id="fadeOutRight4" x1="0" x2="1">
          <stop offset="0" stop-color="var(--rule-blue)"/><stop offset="0.65" stop-color="var(--rule-fade)"/><stop offset="1" stop-color="#ffffff"/>
        </linearGradient>
      </defs>
      <rect x="10" y="214" width="471" height="2" fill="url(#fadeOutRight4)"/>
      <line x1="10" y1="219" x2="481" y2="219" stroke="var(--rule-grey)" stroke-width="1"/>
    </svg>
    <div class="brand"><span class="brand-dot"></span><span class="brand-name">Hearth And Loom</span></div>
    <div class="service-line">THOUGHTFUL DESIGN FOR EVERY ROOM, EVERY PORCH AND EVERY HOME SALE</div>
    <div class="contact" style="top:150px;">
      <div class="contact-name">Carla M Vandrell</div>
      <div class="contact-title">Senior Design Specialist</div>
      <div class="contact-phone">310.574.2936</div>
      <div class="contact-email">carla@hearthandloomhome.com</div>
    </div>
  </section>

</main>
</body>
</html>
```